Powerpoint design for european B2B business

We need a Powerpoint design for a newly established IT company with a B2B focus. We want to develop management information systems that help managers communicate goals into their organization and analyze their organizational activities and performance.

We defined the attached color scale, please relate your design to these colors.

The design should be simple and straight, serious and professional and leave enough space for the content ... :-)

Target Market(s)

B2B, companies larger than 200 employees

Industry/Entity Type

Business

Font styles to use
Sans Serif

Requirements
Should not have
• too playful design, clipart style

```html
<!DOCTYPE html>
<html lang="en">
<head>
<meta charset="utf-8">
<title>Veltaro – Slide Master Set</title>
<link rel="stylesheet" href="https://fonts.googleapis.com/css2?family=Questrial&display=swap">
<style>
  :root {
    --navy: #112a43;
    --navy-mid: #2a4a68;
    --steel: #4f7696;
    --steel-light: #7a9bb6;
    --title-blue: #2b5785;
    --brand-blue: #244c78;
    --brand-grey: #c9c9c9;
    --photo-blue: #5b87b8;
    --photo-warm: #b9b2a8;
    --frame: #555555;
    --paper: #ffffff;
  }
  * { box-sizing: border-box; margin: 0; padding: 0; }
  html, body { width: 1200px; height: 961px; overflow: hidden; background: var(--paper); }
  body { font-family: "Questrial", "Century Gothic", sans-serif; position: relative; }
  .sheet {
    position: absolute; inset: 0;
    border: 1.5px solid var(--frame);
  }
  .slide { position: absolute; width: 529px; height: 396px; background: var(--paper); overflow: hidden; }
  .slide--cover { left: 61px; top: 70px; background: var(--navy); }
  .slide--title-photo-a { left: 610px; top: 70px; }
  .slide--blank { left: 61px; top: 494px; }
  .slide--title-photo-b { left: 610px; top: 494px; }

  .cover__band {
    position: absolute; left: 0; top: 0; width: 100%; height: 73px;
    background: linear-gradient(90deg, #132b45 0%, #8b98a6 35%, #ffffff 62%, #ffffff 100%);
  }
  .cover__brand {
    position: absolute; right: 6px; top: 4px;
    font-size: 58px; letter-spacing: -2px; line-height: 1;
    color: var(--brand-blue);
  }
  .cover__hexes { position: absolute; left: 38px; top: 103px; }
  .cover__title {
    position: absolute; left: 146px; top: 226px;
    font-size: 24px; color: #ffffff; white-space: nowrap;
  }

  .side-strip {
    position: absolute; left: 0; top: 0; width: 92px; height: 100%;
    background:
      radial-gradient(circle at 30% 45%, rgba(140,180,215,.45), transparent 55%),
      linear-gradient(160deg, #2c4258 0%, #4d7596 45%, #5d86a8 65%, #2e465d 100%);
  }
  .side-photo {
    position: absolute; left: 0; width: 92px; height: 64px; bottom: 0;
  }
  .side-photo--desks { background: linear-gradient(180deg, #9ab7dd 0%, var(--photo-blue) 55%, #1e3f78 100%); }
  .side-photo--team { height: 62px; background: linear-gradient(180deg, #e7e4de 0%, var(--photo-warm) 55%, #3a4250 100%); }

  .slide__title {
    position: absolute; left: 111px; top: 24px;
    font-size: 24px; color: var(--title-blue); white-space: nowrap;
  }
  .slide__brand {
    position: absolute; right: 3px; bottom: 10px;
    font-size: 40px; letter-spacing: -1.5px; line-height: 1;
    color: var(--brand-grey);
  }
</style>
</head>
<body>
<div class="sheet">

  <section class="slide slide--cover">
    <div class="cover__band"></div>
    <div class="cover__brand">veltaro</div>
    <svg class="cover__hexes" width="104" height="260" viewBox="0 0 104 260">
      <polygon role="img" aria-label="Photo of business people at a meeting" points="20,0 38,0 47,17 38,35 20,35 11,17" fill="#9aa7b6"/>
      <polygon role="img" aria-label="Photo of a hand pointing at a chart" points="30,38 58,38 72,64 58,90 30,90 16,64" fill="#b9cbe0"/>
      <polygon role="img" aria-label="Photo of an office with computer screens" points="15,94 55,94 75,130 55,166 15,166 -5,130" fill="#8697ab"/>
      <polygon role="img" aria-label="Photo of a handshake in a server room" points="27,169 52,169 64,190 52,212 27,212 15,190" fill="#a9b9c9"/>
      <polygon role="img" aria-label="Image of metal gears" points="12,215 32,215 42,233 32,251 12,251 2,233" fill="#6f7e86"/>
    </svg>
    <h1 class="cover__title">Click to edit Master title style</h1>
  </section>

  <section class="slide slide--title-photo-a">
    <div class="side-strip" role="img" aria-label="Abstract blue network of connected lines"></div>
    <div class="side-photo side-photo--desks" role="img" aria-label="Photo of computer workstations"></div>
    <h2 class="slide__title">Click to edit Master title style</h2>
    <div class="slide__brand">veltaro</div>
  </section>

  <section class="slide slide--blank">
    <div class="side-strip" role="img" aria-label="Abstract blue network of connected lines"></div>
    <div class="slide__brand">veltaro</div>
  </section>

  <section class="slide slide--title-photo-b">
    <div class="side-strip" role="img" aria-label="Abstract blue network of connected lines"></div>
    <div class="side-photo side-photo--team" role="img" aria-label="Photo of a business team working at a desk"></div>
    <h2 class="slide__title">Click to edit Master title style</h2>
    <div class="slide__brand">veltaro</div>
  </section>

</div>
</body>
</html>
```